Water Filtration Company needs a business card design using our existing logo/colours!

We design and manufacture and export specialised water filtration equipment. Our equipment will take unclean dirty water and filters to safe clean drinkable water.
We would like to see designs using our existing logo and colours (see attached "Palette") that represents clean safe drinking water (fresh, clean designs but still professional and modern). Our customers are other businesses who supply water filtration equipment, governments, and private individuals.
BUSINESS CARD DETAILS (Common details):
Tel: + 61 7 55 419 276
www: brindlepeak.com.au
Address: 3/47 Cordwell Parade
Marlow Flats NSW 2593 Australia
(please include the word Australia as we are an international company)
Must include: COMMERCIAL WATER FILTRATION EQUIPMENT
NAME NO 1:
Owen Pritch
General Manager
Mobile: +61 427 38 91 04
Email: owen@brindlepeak.com.au
NAME NO. 2:
Gina Rosk
Business Manager
Mobile: +61 409 572 148
Email: gina@brindlepeak.com.au
Must Have:
1) PRINT READY IN .AI & .PDF FORMATS
2) Also saved in file format .ai (Adobe Illustrator - compatible with CS4)
3) Use existing LOGO & COLOURS: Please use our logo (see attached file)
4) FONTS: we have used Avenir & Helvetica in the past but are open to other font types for the address etc.
Thank you!

```html
<!DOCTYPE html>
<html lang="en">
<head>
<meta charset="utf-8">
<title>Brindlepeak Business Card</title>
<link rel="stylesheet" href="https://fonts.googleapis.com/css2?family=Jura:wght@500;600;700&display=swap">
<style>
  :root {
    --backdrop: #fffbf4;
    --card-front: #06598a;
    --card-back: #049db6;
    --ink-light: #ffffff;
    --ink-soft: rgba(255, 255, 255, 0.92);
    --card-shadow: rgba(40, 30, 10, 0.18);
  }
  html, body {
    margin: 0;
    padding: 0;
    overflow: hidden;
  }
  body {
    width: 1200px;
    height: 1000px;
    background: var(--backdrop);
    position: relative;
    font-family: "Jura", "Trebuchet MS", sans-serif;
    color: var(--ink-light);
  }
  .card {
    position: absolute;
    top: 346px;
    width: 544px;
    height: 307px;
    box-shadow: 0 8px 18px var(--card-shadow);
    box-sizing: border-box;
  }
  .card--front {
    left: 39px;
    background: linear-gradient(135deg, #0a6494 0%, var(--card-front) 60%, #04557f 100%);
  }
  .card--back {
    left: 618px;
    background: linear-gradient(135deg, #08a3ba 0%, var(--card-back) 100%);
  }
  .brand {
    position: absolute;
    left: 40px;
    top: 46px;
    font-weight: 700;
    font-size: 44px;
    letter-spacing: 0.5px;
    line-height: 1;
    color: var(--ink-light);
  }
  .person {
    position: absolute;
    left: 40px;
    top: 150px;
  }
  .person__name {
    font-size: 25px;
    font-weight: 600;
    letter-spacing: 0.6px;
    line-height: 1;
    margin: 0;
  }
  .person__role {
    font-size: 16px;
    font-weight: 500;
    letter-spacing: 0.4px;
    line-height: 1;
    margin: 3px 0 0;
    color: var(--ink-soft);
  }
  .contact {
    position: absolute;
    left: 40px;
    top: 227px;
    font-size: 16px;
    font-weight: 600;
    letter-spacing: 0.3px;
    line-height: 19px;
    color: var(--ink-soft);
  }
  .contact p, .company-info p { margin: 0; }
  .company-info {
    position: absolute;
    left: 53px;
    top: 144px;
    font-size: 16px;
    font-weight: 600;
    letter-spacing: 0.4px;
    color: var(--ink-soft);
  }
  .company-info__tel { line-height: 20px; }
  .company-info__address {
    margin-top: 26px !important;
    line-height: 23px;
  }
  .company-info__web {
    margin-top: 16px !important;
    font-size: 27px;
    letter-spacing: 0.8px;
    line-height: 1;
    color: var(--ink-light);
  }
</style>
</head>
<body>
  <section class="card card--front" aria-label="Business card front">
    <div class="brand">brindlepeak</div>
    <div class="person">
      <p class="person__name">Owen Pritch</p>
      <p class="person__role">General Manager</p>
    </div>
    <div class="contact">
      <p>Mobile: +61 427 38 91 04</p>
      <p>Email: owen@brindlepeak.com.au</p>
    </div>
  </section>

  <section class="card card--back" aria-label="Business card back">
    <div class="company-info">
      <p class="company-info__tel">Tel: + 61 7 55 419 276</p>
      <p class="company-info__address">Address: 3/47 Cordwell Parade<br>Marlow Flats NSW 2593 Australia</p>
      <p class="company-info__web">www: brindlepeak.com.au</p>
    </div>
  </section>
</body>
</html>
```